Business Card design for construction company

I would like a business card design for a construction company - Harlow Constructions. I have attached the ai logo file for use. I would like the card to be very smart and clean and incorporate only white and the two colours in the logo. I would like the card to have two sides. One side can just have the logo, the other with the relevant information.

Target Market(s)

Building and Construction Clients

Industry/Entity Type

Business

Contact Information for Business Card

Name: Tom Pardoe
Company: Harlow Constructions Pty Limited
Address: 14 Mallee Crescent Carrow Vale 2093
Phone: 0427 531 068
Email: tomp@harlowbuild-example.com.au

Font styles to use
Serif
Sans Serif

Requirements
Must have
• Details noted above
• Logo as provided
• Colours as in logo
• Square edges
• A font that compliments the logo
Should not have
• Any colour other than white and those in logo
• Rounded edges

```html
<!DOCTYPE html>
<html lang="en">
<head>
<meta charset="utf-8">
<title>Harlow Constructions – Business Card</title>
<link rel="stylesheet" href="https://fonts.googleapis.com/css2?family=Open+Sans:wght@400;600;700&display=swap">
<style>
  :root {
    --ink: #3b3b3d;
    --ink-soft: #555558;
    --accent: #1c9fe0;
    --paper: #ffffff;
    --backdrop: #e9e9ea;
  }
  * { box-sizing: border-box; margin: 0; padding: 0; }
  html, body {
    width: 1200px; height: 716px; overflow: hidden;
    background: var(--backdrop);
    font-family: "Open Sans", Arial, sans-serif;
    color: var(--ink);
  }
  .sheet { position: relative; width: 1200px; height: 716px; }
  .card {
    position: absolute; top: 200px;
    width: 520px; height: 317px;
    background: var(--paper);
    box-shadow: 0 6px 18px rgba(0,0,0,.18);
    overflow: hidden;
  }
  .card--front { left: 50px; }
  .card--back { left: 630px; }

  .brand {
    position: absolute; display: flex; align-items: center; gap: 12px;
    font-weight: 400; letter-spacing: 4px; text-transform: uppercase;
    color: var(--ink); white-space: nowrap;
  }
  .brand__mark { width: 12px; height: 12px; background: var(--accent); flex: none; }
  .card--front .brand { left: 50%; top: 50%; transform: translate(-50%, -50%); font-size: 24px; }
  .card--back .brand { left: 118px; top: 84px; font-size: 22px; }

  .holder {
    position: absolute; left: 32px; top: 162px;
    font-weight: 700; font-size: 15px; letter-spacing: 1.5px; text-transform: uppercase;
  }
  .rule { position: absolute; left: 26px; top: 188px; width: 470px; height: 2px; background: var(--ink); }
  .contact {
    position: absolute; left: 30px; top: 200px;
    list-style: none; font-size: 12px; color: var(--ink-soft); line-height: 20px;
  }
  .contact li { display: flex; align-items: center; gap: 7px; }
  .contact svg { width: 12px; height: 12px; flex: none; }
  .address {
    position: absolute; right: 22px; top: 208px;
    display: flex; align-items: center; gap: 7px;
    font-size: 12.5px; color: var(--ink-soft);
  }
  .address svg { width: 11px; height: 14px; }
  .accent-line { position: absolute; left: 0; top: 270px; width: 270px; height: 2px; background: var(--accent); }
  .entity-band {
    position: absolute; left: 270px; top: 270px; right: 0; bottom: 0;
    background: var(--accent); color: var(--paper);
    font-weight: 600; font-size: 13px; letter-spacing: 1px;
    display: flex; align-items: center; justify-content: center;
  }
</style>
</head>
<body>
<main class="sheet">
  <section class="card card--front" aria-label="Card front">
    <div class="brand"><span class="brand__mark"></span>Harlow Constructions</div>
  </section>

  <section class="card card--back" aria-label="Card back">
    <div class="brand"><span class="brand__mark"></span>Harlow Constructions</div>
    <h1 class="holder">Tom Pardoe</h1>
    <div class="rule"></div>
    <ul class="contact">
      <li>
        <svg viewBox="0 0 24 24" aria-hidden="true"><path fill="var(--ink)" d="M6.6 10.8a15.1 15.1 0 0 0 6.6 6.6l2.2-2.2a1 1 0 0 1 1-.25 11.4 11.4 0 0 0 3.6.57 1 1 0 0 1 1 1V20a1 1 0 0 1-1 1A17 17 0 0 1 3 4a1 1 0 0 1 1-1h3.5a1 1 0 0 1 1 1c0 1.25.2 2.45.57 3.57a1 1 0 0 1-.25 1z"/></svg>
        0427 531 068
      </li>
      <li>
        <svg viewBox="0 0 24 24" aria-hidden="true"><rect x="2" y="5" width="20" height="14" fill="none" stroke="var(--ink)" stroke-width="2"/><path d="M2 5l10 8 10-8M2 19l7-7M22 19l-7-7" fill="none" stroke="var(--ink)" stroke-width="2"/></svg>
        tomp@harlowbuild-example.com.au
      </li>
    </ul>
    <div class="address">
      <svg viewBox="0 0 20 26" aria-hidden="true"><path fill="var(--ink)" d="M10 0a9 9 0 0 0-9 9c0 7 9 17 9 17s9-10 9-17a9 9 0 0 0-9-9zm0 12.5A3.5 3.5 0 1 1 10 5.5a3.5 3.5 0 0 1 0 7z"/></svg>
      14 Mallee Crescent Carrow Vale 2093
    </div>
    <div class="accent-line"></div>
    <div class="entity-band">Harlow Constructions Pty Limited</div>
  </section>
</main>
</body>
</html>
```